Calm and Compass Health Flyer (new business startup)

One page...clear enough to be read if faxed. This mental health clinic treats depression/anxiety in kids and adults. It also treats opiate and alcohol addiction. It's in downtown Elmira, NY and the owner of the clinic is from Elmira NY, where it's located. This clinic does not take health insurance, so it charges a low rate of $75 a visit once they pay the $125 starting fee.

Target Market(s)

doctors offices, new patients

Industry/Entity Type

Doctor

Requirements
Must have
• see microsoft word document. pdf is printed on the company letterhead.
Nice to have
• a simplified map would be nice. if you can include the building it would be a plus. The same two fonts were used in the business cards and letter head (kennedy small caps boo*) and Refrigerator Delux.

```html
<!DOCTYPE html>
<html lang="en">
<head>
<meta charset="utf-8">
<title>Calm and Compass Health Flyer</title>
<link rel="stylesheet" href="https://fonts.googleapis.com/css2?family=Cinzel:wght@700&family=Saira+Condensed:wght@400;500&display=swap">
<style>
  :root {
    --orange: #ef5b2b;
    --blue: #27a4dc;
    --ink: #1f1f1f;
    --paper: #ffffff;
    --cond: "Saira Condensed", "Arial Narrow", sans-serif;
    --serif: "Cinzel", Georgia, serif;
  }
  * { margin: 0; padding: 0; box-sizing: border-box; }
  html, body { width: 800px; height: 1200px; overflow: hidden; background: var(--paper); }
  .flyer { position: relative; width: 800px; height: 1200px; background: var(--paper); font-family: var(--cond); }

  .brand { position: absolute; top: 66px; right: 30px; display: flex; align-items: center; gap: 10px; }
  .brand-dot { width: 22px; height: 22px; border-radius: 50%; background: var(--orange); }
  .brand-name { font-family: var(--cond); font-weight: 500; font-size: 30px; color: var(--orange); letter-spacing: 0.5px; }

  .head-art { position: absolute; left: 0; top: 0; width: 360px; height: 660px;
    background: linear-gradient(135deg, #f7a07f 0%, #fbd9cb 45%, #bfe4f5 75%, #7ccbeb 100%);
    border-radius: 0 0 180px 0; }

  .building-photo { position: absolute; left: 346px; top: 164px; width: 454px; height: 406px;
    background: linear-gradient(180deg, #b9d7ef 0%, #c9a08a 30%, #8a5140 70%, #6e6a66 100%); }

  .slogan { position: absolute; left: 317px; top: 494px; width: 483px; height: 76px; background: var(--orange);
    color: #fff; font-family: var(--serif); text-align: center; padding-top: 6px; }
  .slogan-main { font-size: 38px; line-height: 40px; }
  .slogan-sub { font-size: 19px; line-height: 22px; }

  .price { position: absolute; top: 651px; width: 214px; height: 256px; border: 3px solid var(--orange);
    border-radius: 6px; overflow: hidden; background: #fff; }
  .price-eval { left: 314px; }
  .price-visit { left: 543px; }
  .price-name { color: var(--blue); font-size: 31px; line-height: 43px; text-align: center; padding-top: 12px; height: 163px; }
  .price-amount { background: var(--orange); color: #fff; font-size: 62px; text-align: center; height: 90px; line-height: 90px; }
  .price-amount sup { font-size: 24px; vertical-align: 28px; }

  .hours { position: absolute; left: 55px; top: 672px; width: 212px; height: 212px; border-radius: 50%;
    background: var(--blue); color: #fff; text-align: center; }
  .hours-ring { position: absolute; inset: 8px; border: 3px dotted #fff; border-radius: 50%; }
  .hours-icon { position: absolute; left: 88px; top: 36px; }
  .hours-text { position: absolute; left: 0; right: 0; top: 88px; font-size: 21px; line-height: 28px; }
  .hours-time { font-size: 36px; line-height: 42px; }

  .ages { position: absolute; left: 314px; top: 927px; width: 486px; height: 76px; background: var(--blue);
    border-radius: 38px 0 0 38px; color: #fff; font-size: 36px; line-height: 76px; padding-left: 70px; letter-spacing: 0.5px; }
  .ages::before { content: ""; position: absolute; left: 24px; top: 29px; width: 18px; height: 18px; border-radius: 50%; background: #fff; }

  .conditions-tag { position: absolute; left: 48px; top: 951px; width: 230px; height: 40px; background: var(--orange);
    border-radius: 14px 14px 0 0; color: #fff; font-size: 27px; line-height: 40px; text-align: center; }
  .conditions-list { position: absolute; left: 20px; top: 1004px; width: 282px; color: var(--blue); font-size: 28px;
    line-height: 38px; text-align: center; }

  .contact { position: absolute; left: 337px; top: 1030px; color: var(--ink); }
  .contact-line { font-size: 31px; line-height: 40px; }
  .contact-address { color: var(--blue); font-size: 16px; line-height: 20px; }

  .map { position: absolute; left: 568px; top: 1028px; width: 192px; height: 100px;
    background: linear-gradient(160deg, #eef1ee 0%, #dfe6e1 55%, #bcd6ea 100%); border: 1px solid #c9c9c9; }

  .disclaimer { position: absolute; left: 337px; top: 1150px; width: 440px; font-family: Arial, sans-serif;
    font-size: 8.5px; line-height: 11px; color: var(--ink); }
</style>
</head>
<body>
<main class="flyer">
  <div class="head-art" role="img" aria-label="Decorative illustration of overlapping orange and blue head profiles with concentric rings"></div>

  <header class="brand">
    <span class="brand-dot"></span>
    <span class="brand-name">CALM AND COMPASS HEALTH</span>
  </header>

  <div class="building-photo" role="img" aria-label="Photograph of the brick clinic building in downtown Elmira"></div>
  <div class="slogan">
    <div class="slogan-main">WE WORK FOR YOU</div>
    <div class="slogan-sub">NOT THE INSURANCE COMPANIES</div>
  </div>

  <section class="price price-eval">
    <div class="price-name">PSYCHIATRIC<br>EVALUATION<br>(45MIN)</div>
    <div class="price-amount">$125<sup>*</sup></div>
  </section>
  <section class="price price-visit">
    <div class="price-name">PSYCHIATRIC<br>OFFICE VISIT<br>(15MIN)</div>
    <div class="price-amount">$75<sup>*</sup></div>
  </section>

  <section class="hours">
    <div class="hours-ring"></div>
    <svg class="hours-icon" width="36" height="40" viewBox="0 0 36 40" aria-hidden="true">
      <rect x="15" y="0" width="6" height="5" fill="#fff"/>
      <circle cx="18" cy="22" r="15" fill="none" stroke="#fff" stroke-width="3"/>
      <path d="M18 13 V22 L24 26" fill="none" stroke="#fff" stroke-width="3" stroke-linecap="round"/>
    </svg>
    <div class="hours-text">MONDAY AND<br>SATURDAYS<div class="hours-time">9-4PM</div></div>
  </section>

  <div class="ages">AGES:&nbsp; 6 YEARS OLD AND UP</div>

  <div class="conditions-tag">Conditions Treated</div>
  <p class="conditions-list">Depression, Anxiety,<br>PTSD, ADHD, Addiction,<br>Bipolar, Childhood Mood<br>Disorders</p>

  <section class="contact">
    <div class="contact-line">(P) 607-555-0142</div>
    <div class="contact-line">(F) 607-555-0178</div>
    <div class="contact-address">250 W. Water St #310 Elmira, NY 14901</div>
  </section>

  <div class="map" role="img" aria-label="Simplified street map showing the clinic location by the river"></div>

  <p class="disclaimer">*Although we do not partner with any Health Insurance Companies at this time, a bill will be provided to you at the time of service for you to submit to your insurance company.</p>
</main>
</body>
</html>
```